Educational Institution needs a new website

A little bit about ourselves:
Brimley College is a multicultural K-12 school with students who represent nearly 30 ethnic and cultural backgrounds. It is one of the fastest growing schools in the City of Canning (in Perth, Western Australia), and offers quality education with a unique school environment at two campuses.
The mission of Brimley College is to equip students with moral values, academic knowledge and 21st century skills. We empower students to unlock their potential to be confident global citizens.
Brimley College strives to educate students in a manner which inspires them to become lifelong learners. We are committed to raising individuals who are tolerant and respectful towards others enabling them to grow into citizens who contribute to the common good of society.
Here are our design goals:
#1: To emphasise the growth of the school from a small school community to a much larger prestigious college.
#2: Have current and prospective parents have a clear understanding of our college’s morals and values and how we differ from other colleges.
#3: Highlight that our school provides a joyful and safe environment, which is highly valued by parents.
#4: Emphasise that our school presents a welcoming atmosphere for parents as we have strong relationships with our community.
#5: Highlight the various after-school activities available to our students, which are provided through the clubs and pastoral care department.
#6: Allow for online registrations and the option of adding student, staff and parent portals.
#7: Follow the existing school colours
We would like to request the design for the home page and a secondary page to see the alternative layouts.
Other information:
Please note that our logo is will be changed slightly in the upcoming weeks. Please keep this in mind while designing.
We will have another contest for the coding of the website.
We want to be able to make amendments and additions to the content of the website in the future and would like to make sure we have a strong communication with the designer.
The existing website is https://www.brimley-example.edu.au/ for reference for school colours and content.
Education

```html
<!DOCTYPE html>
<html lang="en">
<head>
<meta charset="utf-8">
<title>Brimley College — Home</title>
<link rel="stylesheet" href="https://fonts.googleapis.com/css2?family=Montserrat:wght@400;500;600;700;800&display=swap">
<style>
:root{
  --navy:#0d2f5c;
  --deep:#123f78;
  --blue:#1f6fb8;
  --bright:#2b8bd6;
  --sky:#e8f1fa;
  --ink:#1b2533;
  --muted:#5b6675;
  --white:#ffffff;
}
*{box-sizing:border-box;margin:0;padding:0}
html,body{width:1200px;height:3056px;overflow:hidden;background:var(--white)}
body{font-family:"Montserrat",Arial,sans-serif;color:var(--ink)}
.page{position:relative;width:1200px;height:3056px;overflow:hidden}
.abs{position:absolute}

/* header */
.site-header{position:absolute;left:0;top:0;width:1200px;height:118px;background:var(--white);z-index:5}
.brand{position:absolute;left:44px;top:30px;display:flex;align-items:center;gap:12px}
.brand-dot{width:40px;height:40px;border-radius:50%;background:var(--blue)}
.brand-name{font-weight:800;font-size:22px;line-height:1.05;color:var(--blue);letter-spacing:1px;text-transform:uppercase}
.topbar{position:absolute;right:40px;top:20px;display:flex;align-items:center;gap:8px}
.social{width:24px;height:24px;border-radius:50%;background:var(--blue)}
.search{width:140px;height:26px;border:1px solid #c9d6e4;border-radius:13px;margin-left:10px;font-size:11px;color:#8b96a5;padding:6px 12px}
.search-btn{width:26px;height:26px;border-radius:50%;background:var(--blue)}
.main-nav{position:absolute;right:40px;top:74px;display:flex;gap:26px;font-size:14px;font-weight:500;color:var(--ink)}

/* hero */
.hero-photo{position:absolute;left:0;top:112px;width:1200px;height:470px;background:linear-gradient(135deg,#c9b69a 0%,#e7d8c2 35%,#9fb6c8 70%,#d8a989 100%)}

/* portals */
.portal{position:absolute;border-radius:50%;display:flex;flex-direction:column;align-items:center;justify-content:center;text-align:center;font-weight:800;text-transform:uppercase;box-shadow:0 10px 30px rgba(13,47,92,.18)}
.portal small{display:block;font-weight:500;text-transform:none;font-size:13px;margin-top:2px}
.portal-icon{width:30px;height:30px;border:3px solid currentColor;border-radius:50%;margin-bottom:10px}
.portal.side{width:170px;height:170px;background:var(--white);color:var(--blue);font-size:18px;top:524px}
.portal.main{width:230px;height:230px;background:var(--blue);color:var(--white);font-size:22px;left:485px;top:498px;border:8px solid #5fa3e0}

/* about */
.about{position:absolute;left:0;top:780px;width:1200px;text-align:center}
.section-title{font-size:32px;font-weight:700;color:var(--blue);letter-spacing:1px}
.about-lead{font-size:17px;font-weight:700;margin:16px auto 0;width:460px;line-height:1.5}
.about-text{font-size:13px;line-height:1.6;color:var(--muted);width:890px;margin:30px auto 0;text-align:left}
.btn{display:inline-block;background:var(--blue);color:var(--white);font-size:13px;font-weight:600;padding:9px 26px;border-radius:4px;margin-top:34px}

/* side tabs */
.quick-tabs{position:absolute;right:0;top:896px;width:64px;background:var(--blue);border-radius:10px 0 0 10px;padding:10px 8px;display:flex;flex-direction:column;gap:10px}
.quick-tab{height:72px;border-radius:6px;background:var(--white);color:var(--blue);font-size:9px;font-weight:700;writing-mode:vertical-rl;transform:rotate(180deg);display:flex;align-items:center;justify-content:center}

/* campuses */
.campus{position:absolute;top:1306px;width:478px;height:254px}
.campus-photo{width:100%;height:100%}
.campus-label{position:absolute;right:-20px;top:64px;width:170px;height:112px;background:var(--blue);color:var(--white);padding:20px 18px;font-weight:800;font-size:17px;line-height:1.2;text-transform:uppercase;box-shadow:0 8px 20px rgba(0,0,0,.2)}
.live-btn{display:inline-flex;align-items:center;gap:6px;margin-top:12px;background:var(--white);color:var(--blue);font-size:11px;font-weight:600;padding:5px 10px;border-radius:3px;text-transform:none}

/* announcements */
.ann-title{position:absolute;left:0;top:1822px;width:1200px;text-align:center;color:var(--white);font-size:34px;font-weight:600;letter-spacing:2px}
.ann-card{position:absolute;top:1898px;width:328px;height:282px;background:var(--white);border-radius:6px;overflow:hidden;box-shadow:0 10px 26px rgba(0,0,0,.25)}
.ann-photo{width:100%;height:148px}
.ann-body{padding:14px 18px;border-left:5px solid var(--blue);margin:8px 0 0 0;height:118px}
.ann-head{font-size:17px;font-weight:700;color:var(--blue);line-height:1.25}
.ann-meta{display:flex;gap:18px;margin-top:14px;font-size:11px;color:var(--ink)}
.ann-meta span{display:flex;align-items:center;gap:5px}
.next-btn{position:absolute;left:1080px;top:2010px;width:54px;height:54px;border-radius:50%;background:var(--white);box-shadow:0 6px 16px rgba(0,0,0,.25);display:flex;align-items:center;justify-content:center}

/* actions */
.action{position:absolute;top:2472px;width:172px;height:172px;border-radius:50%;background:var(--white);box-shadow:0 10px 28px rgba(13,47,92,.18);display:flex;flex-direction:column;align-items:center;justify-content:center;text-align:center;font-size:13px;font-weight:700;color:var(--ink);text-transform:uppercase;line-height:1.3}
.action.active{background:var(--bright);color:var(--white)}
.action svg{margin-bottom:10px}

/* footer */
.footer-title{position:absolute;left:88px;top:2890px;color:var(--white);font-size:16px;font-weight:800;text-transform:uppercase}
.footer-text{position:absolute;left:88px;top:2920px;width:360px;color:#c9d8ea;font-size:12px;line-height:1.55}
.reg{position:absolute;top:2908px;color:var(--white);text-align:center}
.reg small{display:block;font-size:10px;font-weight:600;color:#c9d8ea;text-transform:uppercase;letter-spacing:.5px}
.reg strong{display:block;font-size:22px;font-weight:800;margin-top:6px}
.footer-bar{position:absolute;left:0;top:3018px;width:1200px;height:38px;background:var(--blue);display:flex;align-items:center;justify-content:space-between;padding:0 88px;font-size:11px;color:var(--white)}
.footer-social{display:flex;gap:8px}
.footer-social i{width:20px;height:20px;border-radius:50%;background:var(--white);display:block}
</style>
</head>
<body>
<div class="page">

  <!-- hero -->
  <div class="hero-photo" role="img" aria-label="Photo of young students working together on a craft activity in a classroom"></div>
  <svg class="abs" style="left:0;top:400px" width="1200" height="300" viewBox="0 0 1200 300" aria-hidden="true">
    <path d="M0 170 C220 90 420 60 600 110 C820 170 1000 60 1200 20 L1200 300 L0 300 Z" fill="#5fa3e0"/>
    <path d="M0 190 C220 110 420 84 600 134 C820 196 1000 90 1200 48 L1200 300 L0 300 Z" fill="#1f6fb8"/>
    <path d="M0 206 C220 130 420 108 600 158 C820 220 1000 116 1200 76 L1200 300 L0 300 Z" fill="#ffffff"/>
  </svg>

  <header class="site-header">
    <div class="brand"><span class="brand-dot"></span><span class="brand-name">Brimley<br>College</span></div>
    <div class="topbar">
      <span class="social"></span><span class="social"></span><span class="social"></span>
      <span class="search">Search</span><span class="search-btn"></span>
    </div>
    <nav class="main-nav">
      <span>About Us</span><span>Learning</span><span>Student Life</span><span>Enrolment</span><span>Community</span><span>News &amp; Events</span><span>Contact Us</span>
    </nav>
  </header>

  <!-- portals -->
  <div class="portal side" style="left:296px"><span class="portal-icon"></span>Student<small>Portal</small></div>
  <div class="portal main"><span class="portal-icon"></span>Staff<small>Portal</small></div>
  <div class="portal side" style="left:734px"><span class="portal-icon"></span>Parent<small>Portal</small></div>

  <!-- about -->
  <section class="about">
    <h2 class="section-title">ABOUT US</h2>
    <p class="about-lead">Lorem Ipsum is simply dummy text of the printing and typesetting industry.</p>
    <p class="about-text">Lorem Ipsum has been the industry's standard dummy text ever since the 1500s, when an unknown printer took a galley of type and scrambled it to make a type specimen book. It has survived not only five centuries, but also the leap into electronic typesetting, remaining essentially unchanged. It was popularised in the 1960s with the release of Letraset sheets containing Lorem Ipsum passages.</p>
    <span class="btn">Read More</span>
  </section>

  <aside class="quick-tabs">
    <span class="quick-tab">Enrol Now</span>
    <span class="quick-tab">Book a Tour</span>
    <span class="quick-tab">Contact Us</span>
  </aside>

  <!-- campuses -->
  <div class="campus" style="left:88px">
    <div class="campus-photo" role="img" aria-label="Photo of the Northvale campus building with garden and trees" style="background:linear-gradient(120deg,#6d8a4f,#c7b48c 55%,#8a9aa8)"></div>
    <div class="campus-label">Northvale<br>Campus<br><span class="live-btn">
      <svg width="10" height="12" viewBox="0 0 10 12"><path d="M5 0a4 4 0 0 0-4 4c0 3 4 8 4 8s4-5 4-8a4 4 0 0 0-4-4z" fill="#1f6fb8"/></svg>Live Location</span></div>
  </div>
  <div class="campus" style="left:620px">
    <div class="campus-photo" role="img" aria-label="Photo of the Eastbrook campus clock tower and grounds" style="background:linear-gradient(180deg,#8fc1ea,#d7e6ef 55%,#7d9a5e)"></div>
    <div class="campus-label">Eastbrook<br>Campus<br><span class="live-btn">
      <svg width="10" height="12" viewBox="0 0 10 12"><path d="M5 0a4 4 0 0 0-4 4c0 3 4 8 4 8s4-5 4-8a4 4 0 0 0-4-4z" fill="#1f6fb8"/></svg>Live Location</span></div>
  </div>

  <!-- announcements band -->
  <svg class="abs" style="left:0;top:1620px" width="1200" height="810" viewBox="0 0 1200 810" aria-hidden="true">
    <defs>
      <linearGradient id="bandFill" x1="0" y1="0" x2="0" y2="1">
        <stop offset="0" stop-color="#1f6fb8"/><stop offset="1" stop-color="#0d2f5c"/>
      </linearGradient>
    </defs>
    <path d="M0 60 C300 -10 600 150 900 90 C1020 66 1120 40 1200 50 L1200 700 C900 600 600 800 300 720 C180 690 80 690 0 700 Z" fill="#5fa3e0"/>
    <path d="M0 90 C300 20 600 180 900 120 C1020 96 1120 70 1200 80 L1200 680 C900 580 600 780 300 700 C180 670 80 670 0 680 Z" fill="url(#bandFill)"/>
  </svg>
  <h2 class="ann-title">ANNOUNCEMENTS</h2>

  <article class="ann-card" style="left:88px">
    <div class="ann-photo" role="img" aria-label="Flyer for the college open day" style="background:linear-gradient(135deg,#d7ecf5,#9ccbe4)"></div>
    <div class="ann-body">
      <h3 class="ann-head">Connecting with our community</h3>
      <div class="ann-meta"><span>&#9635; Nov 30, 2022</span><span>&#9719; 3:30 PM to 4:30 PM</span></div>
    </div>
  </article>
  <article class="ann-card" style="left:436px">
    <div class="ann-photo" role="img" aria-label="Hexagon collage of students at a STEAM fest" style="background:linear-gradient(135deg,#5d7f9c,#a9c2d3 50%,#6b8aa5)"></div>
    <div class="ann-body">
      <h3 class="ann-head">where curiosity inspires solution steam fest</h3>
      <div class="ann-meta"><span>&#9635; Oct 22, 2022</span><span>&#9719; 9 AM to 3 PM</span></div>
    </div>
  </article>
  <article class="ann-card" style="left:784px">
    <div class="ann-photo" role="img" aria-label="Photo of a smiling student in class" style="background:linear-gradient(135deg,#c0392b,#e9a98c 50%,#d9c7b8)"></div>
    <div class="ann-body">
      <h3 class="ann-head">Connecting with our community</h3>
      <div class="ann-meta"><span>&#9635; Nov 30, 2022</span><span>&#9719; 3:30 PM to 4:30 PM</span></div>
    </div>
  </article>
  <div class="next-btn"><svg width="18" height="18" viewBox="0 0 18 18"><path d="M6 3l6 6-6 6" stroke="#1b2533" stroke-width="2.5" fill="none"/></svg></div>

  <!-- quick actions -->
  <div class="action" style="left:174px">
    <svg width="46" height="46" viewBox="0 0 46 46"><rect x="6" y="9" width="34" height="30" rx="3" fill="none" stroke="#1b2533" stroke-width="2.5"/><path d="M6 17h34M14 5v8M32 5v8" stroke="#1b2533" stroke-width="2.5"/></svg>
    Book a<br>Tour</div>
  <div class="action" style="left:398px">
    <svg width="46" height="46" viewBox="0 0 46 46"><rect x="10" y="5" width="26" height="36" rx="2" fill="none" stroke="#1b2533" stroke-width="2.5"/><path d="M16 15h14M16 22h14M16 29h10" stroke="#1b2533" stroke-width="2.5"/></svg>
    Enrolment<br>Application<br>Form</div>
  <div class="action" style="left:624px">
    <svg width="46" height="46" viewBox="0 0 46 46"><path d="M5 12h16v28H5zM25 12h16v28H25z" fill="none" stroke="#1b2533" stroke-width="2.5"/></svg>
    Prospectus</div>
  <div class="action active" style="left:854px">
    <svg width="46" height="46" viewBox="0 0 46 46"><path d="M6 8h28v20H16l-8 7v-7H6z" fill="none" stroke="#fff" stroke-width="2.5"/><text x="20" y="23" font-family="Montserrat,sans-serif" font-size="14" font-weight="700" fill="#fff" text-anchor="middle">?</text></svg>
    FAQ</div>

  <!-- footer -->
  <svg class="abs" style="left:0;top:2730px" width="1200" height="326" viewBox="0 0 1200 326" aria-hidden="true">
    <path d="M0 60 C300 10 600 120 900 60 C1020 36 1120 20 1200 24 L1200 326 L0 326 Z" fill="#5fa3e0"/>
    <path d="M0 90 C300 40 600 150 900 90 C1020 66 1120 50 1200 54 L1200 326 L0 326 Z" fill="#0d2f5c"/>
  </svg>
  <h4 class="footer-title">Information Ribbon</h4>
  <p class="footer-text">Lorem Ipsum is simply dummy text of the printing and typesetting industry. Lorem Ipsum has been the industry's standard dummy text ever since the 1500s, when...</p>
  <div class="reg" style="left:700px;width:220px"><small>CRICOS Provider Number</small><strong>01234X</strong></div>
  <div class="reg" style="left:960px;width:200px"><small>ABN</small><strong>12 345 678 901</strong></div>
  <div class="footer-bar">
    <span>Brimley College. All rights reserved &nbsp;|&nbsp; Privacy &nbsp;|&nbsp; Disclaimer &amp; Copyright © 2022</span>
    <span class="footer-social"><i></i><i></i><i></i></span>
  </div>

</div>
</body>
</html>
```